Flyer für Bikeshop
Zielgruppe
Bikeshop bikevermietung bikereparatur 365/365 offen
Aufgabenstellung
Der beigelegte Flyer sollte professionell gestaltet werden. Gerne sende ich diverse Fotos mit um sie evtl. zu verwenden. Ich habe keine präferenzen. Der Flyer sollte Jugendliche ansprechen. Der Flyer kann auch gänzlich ohne Fotos sein.

```html
<!DOCTYPE html>
<html lang="de">
<head>
<meta charset="utf-8">
<title>Pedalhof – Free Bycycle Skills Training</title>
<link rel="stylesheet" href="https://fonts.googleapis.com/css2?family=Outfit:wght@400;500;700&display=swap">
<style>
  :root {
    --brown: #4a2f27;
    --orange: #d9804a;
    --olive: #c9c42b;
    --olive-pale: #e4e29b;
    --grey: #555555;
    --white: #ffffff;
    --sky-top: #a8b9e2;
    --sky-mid: #e8ecf6;
    --ground: #c7a47a;
  }
  * { margin: 0; padding: 0; box-sizing: border-box; }
  html, body { width: 846px; height: 1200px; overflow: hidden; background: var(--white); }
  body { font-family: "Outfit", sans-serif; color: var(--brown); }
  .flyer { position: relative; width: 846px; height: 1200px; overflow: hidden; background: var(--white); }
  .backdrop { position: absolute; inset: 0; width: 846px; height: 1200px; }

  .brand {
    position: absolute; left: 62px; top: 78px;
    display: flex; align-items: center; gap: 10px;
    font-weight: 700; font-size: 26px; letter-spacing: 4px; color: #111;
  }
  .brand-dot { width: 16px; height: 16px; border-radius: 50%; background: #111; }

  .palette { position: absolute; left: 335px; top: 63px; display: flex; gap: 19px; }
  .palette span { width: 30px; height: 30px; border-radius: 50%; }
  .palette .c1 { background: var(--brown); }
  .palette .c2 { background: var(--orange); }
  .palette .c3 { background: var(--olive); }
  .palette .c4 { background: var(--grey); }

  .headline {
    position: absolute; left: 62px; top: 178px;
    font-weight: 700; font-size: 50px; line-height: 58px; letter-spacing: 0.5px;
    color: var(--brown);
  }
  .headline .accent { color: var(--orange); }

  .info { position: absolute; left: 62px; display: flex; align-items: center; gap: 22px; font-size: 21px; line-height: 27px; color: #1e1a18; }
  .info svg { flex: none; width: 36px; }
  .info-time { top: 343px; }
  .info-age { top: 447px; }

  .pricing { position: absolute; left: 579px; top: 266px; font-size: 21px; line-height: 27px; font-weight: 500; color: var(--brown); }

  .topics {
    position: absolute; left: 577px; top: 712px;
    font-size: 22px; line-height: 26.5px; font-weight: 500; color: var(--white);
    list-style: none;
  }

  .footer {
    position: absolute; left: 0; top: 1078px; width: 846px; height: 55px;
    background: var(--brown); color: var(--white);
    display: flex; align-items: center; padding-left: 68px;
    font-size: 17.5px; letter-spacing: 0.3px;
  }
  .footer .sep { margin: 0 8px; font-size: 12px; }
</style>
</head>
<body>
<main class="flyer">
  <svg class="backdrop" viewBox="0 0 846 1200" xmlns="http://www.w3.org/2000/svg">
    <defs>
      <linearGradient id="photoTone" x1="0" y1="0" x2="0" y2="1">
        <stop offset="0" stop-color="var(--sky-top)"/>
        <stop offset="0.45" stop-color="var(--sky-mid)"/>
        <stop offset="0.78" stop-color="#d9c7a3"/>
        <stop offset="1" stop-color="var(--ground)"/>
      </linearGradient>
    </defs>
    <path class="brush-pale" fill="var(--olive-pale)"
      d="M0 560 L40 552 L90 548 L140 556 L200 548 L260 566 L320 570 L370 580 L360 700 L330 860 L300 1000 L285 1078 L80 1078 L60 1040 L30 1000 L10 960 L0 930 Z"/>
    <path class="photo" role="img" aria-label="Foto: Jugendliche fährt auf einem gelben Mountainbike einen Feldweg unter blauem Himmel"
      fill="url(#photoTone)"
      d="M470 330 L846 330 L846 1200 L265 1200 L290 1080 L300 1000 L330 860 L360 700 L400 560 L440 440 Z"/>
    <path class="brush-olive" fill="var(--olive)"
      d="M440 168 L470 180 L520 175 L560 160 L610 168 L660 155 L720 175 L780 190 L846 205 L846 428 L800 418 L740 405 L680 395 L620 385 L560 378 L520 372 L480 362 L460 330 L450 290 L455 240 L445 200 Z"/>
    <path class="brush-orange" fill="var(--orange)"
      d="M530 697 L600 690 L680 692 L760 697 L758 870 L720 866 L660 860 L600 852 L575 838 L572 810 L535 808 L520 790 L522 740 Z"/>
  </svg>

  <div class="brand"><span class="brand-dot"></span>PEDALHOF</div>

  <div class="palette"><span class="c1"></span><span class="c2"></span><span class="c3"></span><span class="c4"></span></div>

  <h1 class="headline"><span class="accent">FREE</span> BYCYCLE<br>SKILLS <span class="accent">TRAINING</span></h1>

  <div class="info info-time">
    <svg viewBox="0 0 36 40" fill="none" stroke="var(--brown)" stroke-width="1.8" stroke-linecap="round">
      <circle cx="18" cy="20" r="14"/>
      <path d="M6 9 a5 5 0 0 1 7 -3 M30 9 a5 5 0 0 0 -7 -3 M18 20 V13 M18 20 L22 23 M8 33 L6 37 M28 33 L30 37"/>
    </svg>
    <p>Jeden Freitag<br>von 16.30 bis 18.30 Uhr</p>
  </div>

  <div class="info info-age">
    <svg viewBox="0 0 36 46" fill="none" stroke="var(--orange)" stroke-width="3" stroke-linecap="round">
      <path d="M2 26 L16 44 L34 2"/>
    </svg>
    <p>Für alle Jugendlichen<br>von 8-14 Jahren</p>
  </div>

  <p class="pricing">Fahrtraining<br>mit eigenem Bike gratis<br>mit Mietbike Fr. 20,-</p>

  <ul class="topics">
    <li>Bremstraining</li>
    <li>Techniktipps</li>
    <li>Reparaturkurse</li>
    <li>Wheelytraining</li>
  </ul>

  <footer class="footer">
    Pedalhof<span class="sep">•</span>Via Lavinera 14<span class="sep">•</span>7512 Sur Crasta<span class="sep">•</span>kontakt@pedalhof.ch<span class="sep">•</span>081 555 27 90
  </footer>
</main>
</body>
</html>
```